Copperfield interiors PTY LTD

My business specializes in commercial fitout which builds walls, ceilings, doors, uses also materials aluminium in works. Id like to have a logo designed for my company too.

Industry/Entity Type

Business

```html
<!DOCTYPE html>
<html lang="en">
<head>
<meta charset="UTF-8">
<title>Copperfield interiors PTY LTD — Business Card</title>
<link href="https://fonts.googleapis.com/css2?family=Hind:wght@400;500;700&display=swap" rel="stylesheet">
<style>
  :root {
    --brand-blue: #00aeef;
    --ink: #111111;
    --paper: #ffffff;
    --backdrop: #eef0f2;
    --card-shadow: 0 4px 14px rgba(0, 0, 0, 0.18);
  }
  * { box-sizing: border-box; margin: 0; padding: 0; }
  html, body {
    width: 1200px;
    height: 1200px;
    overflow: hidden;
    background: var(--backdrop);
    font-family: "Hind", Arial, sans-serif;
  }
  .canvas {
    position: relative;
    width: 1200px;
    height: 1200px;
  }
  .card {
    position: absolute;
    width: 720px;
    height: 400px;
    box-shadow: var(--card-shadow);
  }
  .card--front { left: 242px; top: 178px; background: var(--paper); }
  .card--back  { left: 241px; top: 638px; background: var(--brand-blue); }

  /* Front: company name block */
  .wordmark {
    position: absolute;
    left: 40px;
    width: 280px;
    top: 160px;
    text-align: center;
    color: var(--brand-blue);
    font-weight: 700;
  }
  .wordmark__name {
    display: block;
    font-size: 38px;
    line-height: 1;
  }
  .wordmark__tagline {
    display: block;
    margin-top: 8px;
    font-size: 14px;
    letter-spacing: 4px;
    line-height: 1;
  }

  /* Front: person + contacts */
  .person {
    position: absolute;
    left: 350px;
    top: 54px;
  }
  .person__name {
    font-size: 39px;
    font-weight: 400;
    color: var(--ink);
    line-height: 1.1;
  }
  .person__role {
    font-size: 24px;
    color: var(--brand-blue);
    line-height: 1.1;
    margin-top: 2px;
  }
  .contacts {
    position: absolute;
    left: 344px;
    top: 166px;
    list-style: none;
  }
  .contacts__item {
    display: flex;
    align-items: center;
    height: 50px;
  }
  .contacts__icon {
    width: 36px;
    height: 36px;
    margin-right: 30px;
    flex-shrink: 0;
  }
  .contacts__text {
    font-size: 22px;
    color: var(--ink);
    line-height: 1;
    padding-top: 4px;
  }

  /* Back */
  .back-mark {
    position: absolute;
    left: 0;
    right: 0;
    top: 148px;
    text-align: center;
    color: var(--paper);
    font-weight: 700;
  }
  .back-mark__name {
    display: block;
    font-size: 78px;
    line-height: 1;
  }
  .back-mark__tagline {
    display: block;
    margin-top: 10px;
    font-size: 28px;
    letter-spacing: 14px;
    line-height: 1;
  }
</style>
</head>
<body>
<main class="canvas">

  <section class="card card--front" aria-label="Business card front">
    <div class="wordmark">
      <span class="wordmark__name">Copperfield</span>
      <span class="wordmark__tagline">interiors PTY LTD</span>
    </div>

    <div class="person">
      <h1 class="person__name">Name Surname</h1>
      <p class="person__role">Description</p>
    </div>

    <ul class="contacts">
      <li class="contacts__item">
        <svg class="contacts__icon" viewBox="0 0 36 36" fill="none" stroke="var(--brand-blue)" stroke-width="1.6" aria-hidden="true">
          <rect x="10" y="2" width="16" height="32" rx="2"/>
          <line x1="10" y1="7" x2="26" y2="7"/>
          <line x1="10" y1="28" x2="26" y2="28"/>
          <line x1="16" y1="4.5" x2="20" y2="4.5"/>
        </svg>
        <span class="contacts__text">0123 456 789</span>
      </li>
      <li class="contacts__item">
        <svg class="contacts__icon" viewBox="0 0 36 36" fill="none" stroke="var(--brand-blue)" stroke-width="1.6" aria-hidden="true">
          <rect x="2" y="8" width="32" height="20" rx="1"/>
          <polyline points="2,8 18,21 34,8"/>
          <line x1="2" y1="28" x2="14" y2="18"/>
          <line x1="34" y1="28" x2="22" y2="18"/>
        </svg>
        <span class="contacts__text">mail@company.com</span>
      </li>
      <li class="contacts__item">
        <svg class="contacts__icon" viewBox="0 0 36 36" fill="none" stroke="var(--brand-blue)" stroke-width="1.6" aria-hidden="true">
          <circle cx="18" cy="18" r="16"/>
          <ellipse cx="18" cy="18" rx="7" ry="16"/>
          <line x1="18" y1="2" x2="18" y2="34"/>
          <line x1="2" y1="18" x2="34" y2="18"/>
          <path d="M5 10 H31 M5 26 H31"/>
        </svg>
        <span class="contacts__text">www.company.com</span>
      </li>
      <li class="contacts__item">
        <svg class="contacts__icon" viewBox="0 0 36 36" fill="none" stroke="var(--brand-blue)" stroke-width="1.6" aria-hidden="true">
          <path d="M18 34 C11 24 5 19 5 13 A13 13 0 0 1 31 13 C31 19 25 24 18 34 Z"/>
          <circle cx="18" cy="13" r="5"/>
        </svg>
        <span class="contacts__text">1234 location , st. city</span>
      </li>
    </ul>
  </section>

  <section class="card card--back" aria-label="Business card back">
    <div class="back-mark">
      <span class="back-mark__name">Copperfield</span>
      <span class="back-mark__tagline">interiors PTY LTD</span>
    </div>
  </section>

</main>
</body>
</html>
```